MOLVT Study flyer

I need help designing a flyer for a research study that will include brain imaging in adolescents. The info is in the attached document. The study is called the Marrowby Orchard Lantern Vesper Trail (MOLVT) study. Ideally this would be returned as a document that I can edit in the future as we will have several new recruitment phases (different age groups, etc. I also would love to have a logo designed as part of this project, but I recognize that might be a separate design request.

```html
<!DOCTYPE html>
<html lang="en">
<head>
<meta charset="utf-8">
<title>MOLVT Study Flyer</title>
<link rel="stylesheet" href="https://fonts.googleapis.com/css2?family=Poppins:ital,wght@0,400;0,600;0,700;1,700&display=swap">
<style>
  :root {
    --navy: #4f5ea8;
    --navy-text: #4a56a3;
    --teal: #2aaeb3;
    --lavender-light: #b7bdf2;
    --lavender: #8e98e2;
    --lavender-deep: #7581d8;
    --ink: #2f3140;
    --white: #ffffff;
  }
  * { margin: 0; padding: 0; box-sizing: border-box; }
  html, body { width: 927px; height: 1200px; overflow: hidden; background: var(--white); }
  body { font-family: "Poppins", sans-serif; color: var(--ink); }
  .flyer { position: relative; width: 927px; height: 1200px; overflow: hidden; background: var(--white); }

  .hero-art { position: absolute; left: 0; top: 0; width: 927px; height: 462px; }

  .study-title { position: absolute; left: 24px; top: 14px; color: var(--navy-text); }
  .study-title .acronym { font-size: 56px; font-weight: 700; letter-spacing: 1px; line-height: 1.05; }
  .study-title .full-name { font-size: 20px; font-weight: 400; line-height: 1.2; width: 330px; margin-top: 2px; }

  .banner { position: absolute; left: 0; color: var(--white); font-weight: 600; border-radius: 0 18px 18px 0; padding-left: 24px; }
  .banner-parent { top: 190px; width: 464px; height: 104px; background: var(--navy); font-size: 39px; line-height: 42px; padding-top: 10px; }
  .banner-worry { top: 306px; width: 441px; height: 148px; background: var(--teal); font-size: 39px; line-height: 42px; padding-top: 9px; }

  .institution { position: absolute; left: 24px; top: 500px; display: flex; align-items: center; gap: 12px; color: var(--navy-text); font-weight: 600; font-size: 24px; line-height: 1.1; }
  .institution .mark { width: 52px; height: 52px; background: var(--navy); }

  .intro { position: absolute; left: 24px; top: 596px; width: 880px; font-size: 17px; line-height: 25px; }

  .section { position: absolute; left: 0; width: 927px; }
  .section h2 { position: relative; font-size: 19.5px; font-weight: 700; font-style: italic; color: var(--navy-text); padding-left: 24px; line-height: 26px; }
  .section h2::before { content: ""; position: absolute; left: 0; top: 5px; width: 16px; height: 17px; background: var(--teal); border-radius: 0 9px 9px 0; }
  .section ul { list-style: none; margin-top: 9px; padding-left: 57px; width: 900px; }
  .section li { position: relative; font-size: 17px; line-height: 27.6px; }
  .section li::before { content: ""; position: absolute; left: -19px; top: 10px; width: 8px; height: 8px; border-radius: 50%; background: var(--teal); }
  .section-involves { top: 673px; }
  .section-eligible { top: 839px; }

  .call-to-action { position: absolute; left: 24px; top: 986px; font-size: 34px; font-weight: 600; line-height: 40px; color: var(--navy-text); }
  .call-to-action .highlight { color: var(--teal); }

  .contact-band { position: absolute; left: 0; top: 1115px; width: 472px; height: 85px; background: var(--navy); display: flex; align-items: center; padding-left: 24px; gap: 12px; color: var(--white); font-size: 20px; padding-bottom: 18px; }
  .contact-band svg { width: 26px; height: 20px; }

  .compensation { position: absolute; left: 471px; top: 1040px; width: 456px; height: 160px; background: var(--teal); border-radius: 44px 0 0 0; color: var(--white); text-align: center; font-weight: 700; padding-top: 20px; }
  .compensation .label { font-size: 40px; line-height: 44px; }
  .compensation .amount { font-size: 60px; line-height: 66px; }
</style>
</head>
<body>
<div class="flyer">
  <svg class="hero-art" viewBox="0 0 927 462" role="img" aria-label="Illustration of two adolescent profiles with visible brains in soft lavender tones">
    <defs>
      <linearGradient id="heroTone" x1="0" y1="0" x2="1" y2="1">
        <stop offset="0" stop-color="var(--lavender-deep)"/>
        <stop offset="0.55" stop-color="var(--lavender)"/>
        <stop offset="1" stop-color="var(--lavender-light)"/>
      </linearGradient>
    </defs>
    <path d="M0 0H927V446Q760 456 510 460L0 460Z" fill="url(#heroTone)"/>
    <path d="M0 0H402C360 110 210 165 0 165Z" fill="var(--white)"/>
  </svg>

  <div class="study-title">
    <div class="acronym">MOLVT</div>
    <div class="full-name">Marrowby Orchard Lantern Vesper Trail</div>
  </div>

  <div class="banner banner-parent">Are you the parent<br>of a child age 10-17?</div>
  <div class="banner banner-worry">Do they worry or<br>overthink negative<br>emotions?</div>

  <div class="institution">
    <span class="mark"></span>
    <span>Halvern State<br>University</span>
  </div>

  <p class="intro">Halvern State University researchers are seeking girls age 10-17 for a study about brain activity in emotions and decision-making and how they relate to puberty, anxiety and depression.</p>

  <section class="section section-involves">
    <h2>Study participation involves</h2>
    <ul>
      <li>One one-hour interview (online or in-person) where your child will discuss their thoughts</li>
      <li>Online questionnaires (parent and child)</li>
      <li>One two-hour visit where your child will complete an MRI scan, answer questions about their puberty stage, and have a small hair sample taken to study puberty hormones</li>
    </ul>
  </section>

  <section class="section section-eligible">
    <h2>Your child may be eligible if they</h2>
    <ul>
      <li>Are age 10-17</li>
      <li>Tend to worry or overthink negative thoughts</li>
      <li>have not been diagnosed with psychosis, learning problems, or autism</li>
    </ul>
  </section>

  <div class="call-to-action">
    Interested in participating?<br>
    Want more information?<br>
    <span class="highlight">Please contact us!</span>
  </div>

  <div class="contact-band">
    <svg viewBox="0 0 26 20" aria-hidden="true">
      <rect x="0" y="0" width="26" height="20" rx="2" fill="var(--white)"/>
      <path d="M1.5 2L13 11L24.5 2" fill="none" stroke="var(--navy)" stroke-width="2.2"/>
    </svg>
    <span>molvtstudy@halvernhealth.edu</span>
  </div>

  <div class="compensation">
    <div class="label">COMPENSATION</div>
    <div class="amount">UP TO $140</div>
  </div>
</div>
</body>
</html>
```